REVISED : Logo & Stationery design for Naturopath

1. I need a logo and stationery (A4 letterhead, Business card & postcard size card for voucher/birthday/reminder use) for my new clinic. 
2. Overall look / logo needs to achieve: sense of personal attention (handwriting like script use somewhere), be unfussy, elegant, professional, modern. calm.
3. MUST be DIFFERENT to what we normally see for naturopaths.
4. Logo will be used eventually on new website so must lend itself to that use.
5. Possible tag lines 'Health is in your nature' or 'Health for generations' = general themes
6. Should appeal to men, mothers, women, depressed, families
Please feel free to submit logo designs prior to stationery work up if preferred.  

Thanks for your designs.  I have updated my brief a little, I hope that it now gives a clearer picture of what I'm looking for.  Have a great day! Marion

Hi Everyone.  I have uploaded some dandelion to give you an idea of the symmetry, perfection and airiness that I'm looking for.

heading away for a week, so apologies to extend the deadline.  Decision will be made on Friday.  Thanks for your patience.

My clients are aged from 5m to 75 years and have an array of problems. My main interest is joint and general inflammation and the role of genetic heritage and nutrigenomics. I follow an evidence based approach. Have a look at www.marionkestle.com.au

Must have
1. some script based font 
2.  colours of nature . 
3. Trading Name: Marion Kestle Naturopathy 
4. Company Name: Brightwell Stride Partners Pty Ltd ABN: 58 217 630 914 (these must be on for legal reasons but not form part of logo or overall company name. 
5. Mailing Address: PO Box 4392, Tallow Ridge NSW 1590 
6. Clinic Address: TBC 
7. Tel: 1300 48 29 63 
8. e: naturopathy@marionkestle.com.au 
9. w: marionkestle.com.au
Business Card and Postcard do not need ABN & Pty Ltd name.
Business Card should have my qualifications: Bachelor of Health Science (Complementary Medicine), ND.
Nice to have
1. design able to be embossed (card, business card)
2. able to be used on non-bleached recycled paper 
3. suitable of matt / uncoated card
4. good for vegetable dye printing
5. concept I really like is of a dandelion blowing in the wind (themes = herb, wistful, dissemination of information, free and easy) 
6. also really like idea of a 'tree of life'
7. but your interpretation of something entirely different might be a winner
8. Use of either of the tag lines 
9. Monochromatic 
Should not have
1. photos
2. more than 3 colours
3. Leaves (too much like every other Naturopath)

```html
<!DOCTYPE html>
<html lang="en">
<head>
<meta charset="utf-8">
<title>Marion Kestle Naturopathy – Logo &amp; Stationery</title>
<link rel="stylesheet" href="https://fonts.googleapis.com/css2?family=Roboto+Condensed:wght@300;400;700&display=swap">
<style>
  :root {
    --green: #7a9240;
    --green-light: #b9c96a;
    --brown: #5a4629;
    --cream: #f2efdf;
    --ornament: #dcd3c3;
    --ink: #1d1a15;
    --edge: #6f6a5f;
  }
  * { margin: 0; padding: 0; box-sizing: border-box; }
  html, body { width: 787px; height: 1200px; overflow: hidden; background: #ffffff; }
  body { position: relative; font-family: "Roboto Condensed", "Arial Narrow", sans-serif; color: var(--ink); }

  .wordmark { position: absolute; color: var(--green); font-weight: 400; line-height: 1; display: flex; align-items: center; gap: 8px; }
  .wordmark .lines { display: flex; flex-direction: column; }
  .wordmark .dot { width: 10px; height: 10px; border-radius: 50%; background: currentColor; flex: none; }

  .wordmark--primary { left: 60px; top: 82px; font-size: 34px; }
  .wordmark--alternate { left: 420px; top: 94px; font-size: 34px; }

  .letterhead {
    position: absolute; left: 51px; top: 217px; width: 679px; height: 960px;
    background: var(--cream); border: 0.6px solid var(--edge);
    box-shadow: 2px 3px 5px rgba(0,0,0,0.18);
    overflow: hidden;
  }
  .letterhead .tagline { position: absolute; left: 48px; top: 23px; font-size: 10px; font-weight: 700; color: var(--brown); letter-spacing: 0.4px; }
  .letterhead .wordmark { left: 318px; top: 34px; font-size: 13px; }
  .letterhead .flourish-top { position: absolute; left: 0; top: 52px; width: 262px; height: 82px; }
  .letterhead .flourish-bottom { position: absolute; left: 430px; top: 840px; width: 249px; height: 120px; }
  .letterhead .footer {
    position: absolute; left: 0; right: 0; top: 907px; text-align: center;
    color: var(--brown); font-weight: 700; font-size: 9.6px; line-height: 11.6px; letter-spacing: 0.6px;
  }

  .card {
    position: absolute; width: 306px; height: 187px; background: var(--cream);
    border: 0.6px solid var(--edge); box-shadow: 2px 3px 5px rgba(0,0,0,0.22); overflow: hidden;
  }
  .card .name { font-size: 13px; font-weight: 400; color: var(--ink); line-height: 1.1; }
  .card .credentials { font-size: 7px; font-weight: 700; color: var(--ink); line-height: 1.3; }
  .card .tagline { color: var(--green); font-size: 9px; font-weight: 400; letter-spacing: 0.3px; }
  .card .contact { font-size: 7.4px; line-height: 10px; color: var(--ink); letter-spacing: 0.2px; }

  .card--banded { left: 291px; top: 492px; }
  .card--banded .band { position: absolute; left: 0; top: 0; width: 100%; height: 70px; background: var(--green); }
  .card--banded .wordmark { left: 16px; top: 24px; font-size: 13px; color: var(--cream); }
  .card--banded .band-flourish { position: absolute; left: 186px; top: 0; width: 102px; height: 70px; }
  .card--banded .identity { position: absolute; right: 187px; top: 126px; text-align: right; }
  .card--banded .details { position: absolute; left: 158px; top: 101px; }
  .card--banded .details .tagline { margin-bottom: 3px; }

  .card--open { left: 449px; top: 699px; }
  .card--open .flourish { position: absolute; left: 106px; top: 20px; width: 200px; height: 167px; }
  .card--open .wordmark { left: 18px; top: 38px; font-size: 14px; }
  .card--open .identity { position: absolute; right: 17px; top: 69px; text-align: right; }
  .card--open .contact { position: absolute; right: 17px; top: 124px; text-align: right; }
  .card--open .tagline { position: absolute; left: 18px; top: 162px; }
</style>
</head>
<body>

  <div class="wordmark wordmark--primary">
    <div class="lines"><span>Marion Kestle</span><span>Naturopathy</span></div>
  </div>

  <div class="wordmark wordmark--alternate">
    <div class="lines"><span>Marion Kestle</span><span>Naturopathy</span></div>
    <span class="dot"></span>
  </div>

  <section class="letterhead">
    <p class="tagline">Health is in your nature</p>
    <div class="wordmark">
      <div class="lines"><span>Marion Kestle</span><span>Naturopathy</span></div>
    </div>
    <svg class="flourish-top" role="img" aria-label="Faint curling vine ornament sweeping across the top left" viewBox="0 0 262 82">
      <defs>
        <linearGradient id="fadeTop" x1="0" y1="0" x2="1" y2="0">
          <stop offset="0" stop-color="#dcd3c3" stop-opacity="0.55"/>
          <stop offset="1" stop-color="#dcd3c3" stop-opacity="0"/>
        </linearGradient>
      </defs>
      <rect width="262" height="82" fill="url(#fadeTop)"/>
    </svg>
    <svg class="flourish-bottom" role="img" aria-label="Faint curling vine ornament in the bottom right corner" viewBox="0 0 249 120">
      <defs>
        <linearGradient id="fadeBottom" x1="1" y1="1" x2="0" y2="0">
          <stop offset="0" stop-color="#dcd3c3" stop-opacity="0.55"/>
          <stop offset="1" stop-color="#dcd3c3" stop-opacity="0"/>
        </linearGradient>
      </defs>
      <rect width="249" height="120" fill="url(#fadeBottom)"/>
    </svg>
    <div class="footer">
      <p>Marion Kestle Naturopathy</p>
      <p>Brightwell Stride Partners Pty Ltd; ABN: 58 217 630 914; PO Box 4392, Tallow Ridge NSW 1590; Clinic Address: TBC; Tel: 1300 48 29 63</p>
      <p>e: naturopathy@marionkestle.com.au; w: marionkestle.com.au</p>
    </div>
  </section>

  <section class="card card--banded">
    <div class="band"></div>
    <div class="wordmark">
      <div class="lines"><span>Marion Kestle</span><span>Naturopathy</span></div>
    </div>
    <svg class="band-flourish" role="img" aria-label="Pale curling vine ornament on the green band" viewBox="0 0 102 70">
      <defs>
        <radialGradient id="fadeBand" cx="0.5" cy="0.5" r="0.6">
          <stop offset="0" stop-color="#f2efdf" stop-opacity="0.28"/>
          <stop offset="1" stop-color="#f2efdf" stop-opacity="0"/>
        </radialGradient>
      </defs>
      <rect width="102" height="70" fill="url(#fadeBand)"/>
    </svg>
    <div class="identity">
      <p class="name">Marion Kestle</p>
      <p class="credentials">Bachelor of Health Science, ND</p>
    </div>
    <div class="details">
      <p class="tagline">Health is in your nature</p>
      <div class="contact">
        <p>PO Box 4392, Tallow Ridge NSW 1590</p>
        <p>clinic address: TBC</p>
        <p>tel: 1300 48 29 63</p>
        <p>e: naturopathy@marionkestle.com.au</p>
        <p>w: marionkestle.com.au</p>
      </div>
    </div>
  </section>

  <section class="card card--open">
    <svg class="flourish" role="img" aria-label="Faint curling vine ornament sweeping up the right side" viewBox="0 0 200 167">
      <defs>
        <linearGradient id="fadeCard" x1="0" y1="1" x2="1" y2="0">
          <stop offset="0" stop-color="#dcd3c3" stop-opacity="0"/>
          <stop offset="0.5" stop-color="#dcd3c3" stop-opacity="0.35"/>
          <stop offset="1" stop-color="#dcd3c3" stop-opacity="0"/>
        </linearGradient>
      </defs>
      <rect width="200" height="167" fill="url(#fadeCard)"/>
    </svg>
    <div class="wordmark">
      <div class="lines"><span>Marion Kestle</span><span>Naturopathy</span></div>
      <span class="dot"></span>
    </div>
    <div class="identity">
      <p class="name">Marion Kestle</p>
      <p class="credentials">Bachelor of Health Science, ND</p>
    </div>
    <div class="contact">
      <p>PO Box 4392, Tallow Ridge NSW 1590</p>
      <p>clinic address: TBC</p>
      <p>tel: 1300 48 29 63</p>
      <p>e: naturopathy@marionkestle.com.au</p>
      <p>w: marionkestle.com.au</p>
    </div>
    <p class="tagline">Health is in your nature</p>
  </section>

</body>
</html>
```